Company selling food supplements with CBD needs label.

We need a label design for a company called "VEX Lab ltd", is based in the UK, the market name is "VEX" or "VEX Velvet Ember Xtracts". The initial product is Virgin Organic Hemp Seed Oil with a CBD in a 10ml amber dropper bottle. The design should be simplicity and luxury. The design should include also box.

Target Market(s)

Food supplements on Pellmart UK

Industry/Entity Type

Supplement

Font styles to use
Other font styles liked:
• Some luxury

Colors

Designer to choose colors to be used in the design.

Requirements
Must have
• All the information on the label required by the UK for the food supplements, the same on the box. One version matt one transparent. The design should include different CBD content, one different bottle (250mg, 500mg, 750mg, 1000mg) .
• The label and box should include the following phrases: "DIRECTIONS: Food Supplement. Shake well before use. Use 4-6 drops 2-3 times a day. Leave the oil in your mouth for 30-60 seconds before swallowing. Gradually build up the dose to find your optimum dosage.
• CAUTION: Do not exceed the recommended daily intake. Do not use as a substitute for a varied diet. Do not use during pregnancy and breastfeeding. Store in a dark and cool place, away from sunlight. Keep away from children.
• INGREDIENTS: Hemp Seed Oil, Omega-6 (2800mg), Omega-3 (930mg), CBD (250mg)
• MANUFACTURED: VEX Lab Ltd, 87 Quillon Rd, Elmcote, KT9 4PW, www,vexlabuk.co.uk, info@vexlabuk.co.uk.
• EXPIRED DATE: "
• The box should also include a place for bark code.
Nice to have
• Simple and elegant design vertical or horizontal with exposed company logo "VEX" or "VEX Velvet Ember Xtracts". The company logo is provided but designers may change it freely.
Should not have
• The best without pictures/graphics overloading simplicity and purity of design.

```html
<!DOCTYPE html>
<html lang="en">
<head>
<meta charset="utf-8">
<title>VEX Hemp Seed Oil – Box Dielines</title>
<link rel="stylesheet" href="https://fonts.googleapis.com/css2?family=Roboto:wght@300;500&family=Oswald:wght@500&display=swap">
<style>
  :root {
    --paper: #ffffff;
    --ink: #ffffff;
    --panel: #050505;
    --badge-ink: #111111;
  }
  html, body {
    margin: 0; padding: 0;
    width: 1200px; height: 1125px;
    overflow: hidden;
    background: var(--paper);
  }
  .stage {
    position: relative;
    width: 1160px; height: 1088px;
    transform: scale(1.0345);
    transform-origin: 0 0;
  }
  .theme-green  { --glow: #1db45a; --accent: #2e9b4e; --badge: #6bbf63; }
  .theme-red    { --glow: #b3232c; --accent: #dd4640; --badge: #e8645c; }
  .theme-yellow { --glow: #efe30c; --accent: #e6da1e; --badge: #f2ea2a; }

  .dieline {
    position: absolute;
    width: 620px; height: 835px;
    transform-origin: 0 0;
    font-family: "Roboto", Arial, sans-serif;
    font-weight: 300;
    color: var(--ink);
  }
  .dieline.main-size { left: 52px; top: 123px; }
  .dieline.red-size { left: 713px; top: 20px; transform: scale(0.613); }
  .dieline.yellow-size { left: 716px; top: 553px; transform: scale(0.613); }

  .box-shape { position: absolute; left: 0; top: 0; }

  .side-strip {
    position: absolute; left: 0; top: 0;
    width: 155px; height: 835px;
    border-radius: 24px;
    background:
      radial-gradient(ellipse 95px 120px at 78px 105px, color-mix(in srgb, var(--glow) 85%, transparent), transparent 100%),
      radial-gradient(ellipse 95px 90px at 78px 735px, color-mix(in srgb, var(--glow) 70%, transparent), transparent 100%),
      var(--panel);
  }
  .strip-logo {
    position: absolute; left: 0; top: 70px; width: 155px;
    text-align: center; font-weight: 500;
  }
  .strip-logo .brand-name { display: block; font-size: 60px; line-height: 60px; letter-spacing: 1px; }
  .strip-logo .brand-tag {
    display: block; margin-top: 1px;
    font-family: "Oswald", "Arial Narrow", sans-serif; font-size: 11px; line-height: 13px;
  }

  .volume { position: absolute; left: 6px; top: 193px; font-size: 18px; }
  .caution {
    position: absolute; left: 6px; top: 256px; width: 138px;
    font-size: 13.6px; line-height: 17px;
  }
  .caution p { margin: 0 0 8px; }
  .caution .storage { width: 150px; font-size: 12.4px; line-height: 15px; }
  .maker {
    position: absolute; left: 10px; top: 537px; width: 145px;
    font-size: 13px; line-height: 15.5px;
  }
  .maker .maker-label { font-size: 12.5px; }
  .maker .maker-name { font-size: 18px; line-height: 22px; }
  .strip-product {
    position: absolute; left: 0; top: 698px; width: 155px;
    text-align: center; font-size: 15px; line-height: 19px;
  }

  .front-logo {
    position: absolute; left: 70px; top: 368px;
    width: 290px; height: 96px;
    transform: rotate(-90deg);
    font-weight: 500;
  }
  .front-logo .brand-name {
    position: absolute; left: 0; top: 0; width: 290px;
    font-size: 132px; line-height: 100px; text-align: center; letter-spacing: 6px;
  }
  .front-tag {
    position: absolute; left: 145px; top: 400px;
    width: 280px; height: 30px;
    transform: rotate(-90deg);
    font-family: "Oswald", "Arial Narrow", sans-serif;
    font-weight: 500; font-size: 25px; line-height: 30px; text-align: center;
  }

  .leaf-art {
    position: absolute; left: 318px; top: 232px;
    width: 140px; height: 125px; border-radius: 50%;
    background: radial-gradient(ellipse at 50% 55%, #4f8f3a 0%, #2c5e26 35%, rgba(20,50,20,0.4) 65%, transparent 72%);
  }
  .product-name {
    position: absolute; left: 310px; top: 370px; width: 150px;
    text-align: center; font-size: 19px; line-height: 23px;
  }
  .cbd-badge {
    position: absolute; left: 334px; top: 457px;
    width: 104px; height: 32px; border-radius: 16px;
    background: var(--badge); color: var(--badge-ink);
    font-family: "Oswald", "Arial Narrow", sans-serif; font-weight: 500;
    font-size: 18px; line-height: 32px; text-align: center; white-space: nowrap;
  }

  .back-panel { position: absolute; left: 469px; top: 243px; width: 146px; font-size: 12.8px; line-height: 15.3px; }
  .back-panel h3 {
    margin: 0; font-weight: 300; font-size: 18px; line-height: 22px;
    border-bottom: 2px solid var(--accent);
  }
  .back-panel p { margin: 2px 0 0; }
  .back-panel .ingredients { margin-top: 6px; }
  .ingredient-list { margin: 2px 0 0; padding: 0; list-style: none; }
  .ingredient-list li span { display: inline-block; width: 62px; }
  .dates { margin-top: 3px; padding-top: 3px; border-top: 2px solid var(--accent); }
</style>
</head>
<body>
<main class="stage">

  <section class="dieline main-size theme-green" aria-label="Box dieline, green edition">
    <svg class="box-shape" width="620" height="835" viewBox="0 0 620 835" aria-hidden="true">
      <defs>
        <radialGradient id="glow-green" cx="178" cy="400" r="190" gradientUnits="userSpaceOnUse">
          <stop offset="0" style="stop-color:var(--glow)"/>
          <stop offset="0.45" style="stop-color:var(--glow);stop-opacity:0.35"/>
          <stop offset="1" style="stop-color:var(--glow);stop-opacity:0"/>
        </radialGradient>
        <radialGradient id="spot-green" cx="558" cy="552" r="40" gradientUnits="userSpaceOnUse">
          <stop offset="0" style="stop-color:var(--glow);stop-opacity:0.8"/>
          <stop offset="1" style="stop-color:var(--glow);stop-opacity:0"/>
        </radialGradient>
        <linearGradient id="line-green" x1="0" x2="1">
          <stop offset="0" style="stop-color:var(--glow);stop-opacity:0"/>
          <stop offset="0.5" style="stop-color:var(--glow)"/>
          <stop offset="1" style="stop-color:var(--glow);stop-opacity:0"/>
        </linearGradient>
      </defs>
      <g fill="#050505">
        <rect x="155" y="157" width="152" height="523" rx="24"/>
        <rect x="465" y="157" width="155" height="523" rx="24"/>
        <rect x="155" y="185" width="465" height="467"/>
      </g>
      <rect x="155" y="185" width="465" height="467" fill="url(#glow-green)"/>
      <rect x="155" y="185" width="465" height="467" fill="url(#spot-green)"/>
      <rect x="240" y="184" width="300" height="2" fill="url(#line-green)"/>
      <rect x="200" y="640" width="360" height="2" fill="url(#line-green)"/>
    </svg>
    <div class="side-strip"></div>
    <div class="strip-logo"><span class="brand-name">VEX</span><span class="brand-tag">Velvet Ember Xtracts</span></div>
    <div class="volume">10 Ml.</div>
    <div class="caution">
      <p>CAUTION:<br>Do not exceed the recommended daily intake.<br>Do not use as a substitute for a varied diet.<br>Do not use during pregnancy and breastfeeding.</p>
      <p class="storage">Store in a dark and cool place, away from sunlight. Keep away from children.</p>
    </div>
    <div class="maker">
      <span class="maker-label">MANUFACTURED BY:</span><br>
      <span class="maker-name">VEX LAB. LTD.</span><br>
      87 Quillon Rd, Elmcote,<br>KT9 4PW<br>www.vexlabuk.co.uk,<br>info@vexlabuk.co.uk
    </div>
    <div class="strip-product">Virgin<br>Organic<br>Hemp seed Oil</div>
    <div class="front-logo"><span class="brand-name">VEX</span></div>
    <div class="front-tag">Velvet Ember Xtracts</div>
    <div class="leaf-art" role="img" aria-label="Hemp leaf illustration"></div>
    <div class="product-name">Virgin<br>Organic<br>Hemp seed Oil</div>
    <div class="cbd-badge">CBD 250mg</div>
    <div class="back-panel">
      <h3>DIRECTIONS:</h3>
      <p>Food Supplement.<br>Shake well before use.<br>Use 4-6 drops 2-3 times<br>a day.<br>Leave the oil in your Mouth for 30-60 Seconds before swallowing.<br>Gradually build up the dose to find your optimum dosage.</p>
      <h3 class="ingredients">INGREDIENTS:</h3>
      <ul class="ingredient-list">
        <li>Hemp Seed Oil</li>
        <li><span>Omega-6</span>-- 2800mg</li>
        <li><span>Omega-3</span>-- 930mg</li>
        <li><span>CBD</span>-- 250mg</li>
      </ul>
      <div class="dates">Date of Mfg.&nbsp; 18.12.2019<br>Date of Exp.&nbsp;&nbsp; 18-12-2021</div>
    </div>
  </section>

  <section class="dieline red-size theme-red" aria-label="Box dieline, red edition">
    <svg class="box-shape" width="620" height="835" viewBox="0 0 620 835" aria-hidden="true">
      <defs>
        <radialGradient id="glow-red" cx="178" cy="400" r="190" gradientUnits="userSpaceOnUse">
          <stop offset="0" style="stop-color:var(--glow)"/>
          <stop offset="0.45" style="stop-color:var(--glow);stop-opacity:0.35"/>
          <stop offset="1" style="stop-color:var(--glow);stop-opacity:0"/>
        </radialGradient>
        <radialGradient id="spot-red" cx="558" cy="552" r="40" gradientUnits="userSpaceOnUse">
          <stop offset="0" style="stop-color:var(--glow);stop-opacity:0.8"/>
          <stop offset="1" style="stop-color:var(--glow);stop-opacity:0"/>
        </radialGradient>
        <linearGradient id="line-red" x1="0" x2="1">
          <stop offset="0" style="stop-color:var(--glow);stop-opacity:0"/>
          <stop offset="0.5" style="stop-color:var(--glow)"/>
          <stop offset="1" style="stop-color:var(--glow);stop-opacity:0"/>
        </linearGradient>
      </defs>
      <g fill="#050505">
        <rect x="155" y="157" width="152" height="523" rx="24"/>
        <rect x="465" y="157" width="155" height="523" rx="24"/>
        <rect x="155" y="185" width="465" height="467"/>
      </g>
      <rect x="155" y="185" width="465" height="467" fill="url(#glow-red)"/>
      <rect x="155" y="185" width="465" height="467" fill="url(#spot-red)"/>
      <rect x="240" y="184" width="300" height="2" fill="url(#line-red)"/>
      <rect x="200" y="640" width="360" height="2" fill="url(#line-red)"/>
    </svg>
    <div class="side-strip"></div>
    <div class="strip-logo"><span class="brand-name">VEX</span><span class="brand-tag">Velvet Ember Xtracts</span></div>
    <div class="volume">10 Ml.</div>
    <div class="caution">
      <p>CAUTION:<br>Do not exceed the recommended daily intake.<br>Do not use as a substitute for a varied diet.<br>Do not use during pregnancy and breastfeeding.</p>
      <p class="storage">Store in a dark and cool place, away from sunlight. Keep away from children.</p>
    </div>
    <div class="maker">
      <span class="maker-label">MANUFACTURED BY:</span><br>
      <span class="maker-name">VEX LAB. LTD.</span><br>
      87 Quillon Rd, Elmcote,<br>KT9 4PW<br>www.vexlabuk.co.uk,<br>info@vexlabuk.co.uk
    </div>
    <div class="strip-product">Virgin<br>Organic<br>Hemp seed Oil</div>
    <div class="front-logo"><span class="brand-name">VEX</span></div>
    <div class="front-tag">Velvet Ember Xtracts</div>
    <div class="leaf-art" role="img" aria-label="Hemp leaf illustration"></div>
    <div class="product-name">Virgin<br>Organic<br>Hemp seed Oil</div>
    <div class="cbd-badge">CBD 250mg</div>
    <div class="back-panel">
      <h3>DIRECTIONS:</h3>
      <p>Food Supplement.<br>Shake well before use.<br>Use 4-6 drops 2-3 times<br>a day.<br>Leave the oil in your Mouth for 30-60 Seconds before swallowing.<br>Gradually build up the dose to find your optimum dosage.</p>
      <h3 class="ingredients">INGREDIENTS:</h3>
      <ul class="ingredient-list">
        <li>Hemp Seed Oil</li>
        <li><span>Omega-6</span>-- 2800mg</li>
        <li><span>Omega-3</span>-- 930mg</li>
        <li><span>CBD</span>-- 250mg</li>
      </ul>
      <div class="dates">Date of Mfg.&nbsp; 18.12.2019<br>Date of Exp.&nbsp;&nbsp; 18-12-2021</div>
    </div>
  </section>

  <section class="dieline yellow-size theme-yellow" aria-label="Box dieline, yellow edition">
    <svg class="box-shape" width="620" height="835" viewBox="0 0 620 835" aria-hidden="true">
      <defs>
        <radialGradient id="glow-yellow" cx="178" cy="400" r="190" gradientUnits="userSpaceOnUse">
          <stop offset="0" style="stop-color:var(--glow)"/>
          <stop offset="0.45" style="stop-color:var(--glow);stop-opacity:0.35"/>
          <stop offset="1" style="stop-color:var(--glow);stop-opacity:0"/>
        </radialGradient>
        <radialGradient id="spot-yellow" cx="558" cy="552" r="40" gradientUnits="userSpaceOnUse">
          <stop offset="0" style="stop-color:var(--glow);stop-opacity:0.8"/>
          <stop offset="1" style="stop-color:var(--glow);stop-opacity:0"/>
        </radialGradient>
        <linearGradient id="line-yellow" x1="0" x2="1">
          <stop offset="0" style="stop-color:var(--glow);stop-opacity:0"/>
          <stop offset="0.5" style="stop-color:var(--glow)"/>
          <stop offset="1" style="stop-color:var(--glow);stop-opacity:0"/>
        </linearGradient>
      </defs>
      <g fill="#050505">
        <rect x="155" y="157" width="152" height="523" rx="24"/>
        <rect x="465" y="157" width="155" height="523" rx="24"/>
        <rect x="155" y="185" width="465" height="467"/>
      </g>
      <rect x="155" y="185" width="465" height="467" fill="url(#glow-yellow)"/>
      <rect x="155" y="185" width="465" height="467" fill="url(#spot-yellow)"/>
      <rect x="240" y="184" width="300" height="2" fill="url(#line-yellow)"/>
      <rect x="200" y="640" width="360" height="2" fill="url(#line-yellow)"/>
    </svg>
    <div class="side-strip"></div>
    <div class="strip-logo"><span class="brand-name">VEX</span><span class="brand-tag">Velvet Ember Xtracts</span></div>
    <div class="volume">10 Ml.</div>
    <div class="caution">
      <p>CAUTION:<br>Do not exceed the recommended daily intake.<br>Do not use as a substitute for a varied diet.<br>Do not use during pregnancy and breastfeeding.</p>
      <p class="storage">Store in a dark and cool place, away from sunlight. Keep away from children.</p>
    </div>
    <div class="maker">
      <span class="maker-label">MANUFACTURED BY:</span><br>
      <span class="maker-name">VEX LAB. LTD.</span><br>
      87 Quillon Rd, Elmcote,<br>KT9 4PW<br>www.vexlabuk.co.uk,<br>info@vexlabuk.co.uk
    </div>
    <div class="strip-product">Virgin<br>Organic<br>Hemp seed Oil</div>
    <div class="front-logo"><span class="brand-name">VEX</span></div>
    <div class="front-tag">Velvet Ember Xtracts</div>
    <div class="leaf-art" role="img" aria-label="Hemp leaf illustration"></div>
    <div class="product-name">Virgin<br>Organic<br>Hemp seed Oil</div>
    <div class="cbd-badge">CBD 250mg</div>
    <div class="back-panel">
      <h3>DIRECTIONS:</h3>
      <p>Food Supplement.<br>Shake well before use.<br>Use 4-6 drops 2-3 times<br>a day.<br>Leave the oil in your Mouth for 30-60 Seconds before swallowing.<br>Gradually build up the dose to find your optimum dosage.</p>
      <h3 class="ingredients">INGREDIENTS:</h3>
      <ul class="ingredient-list">
        <li>Hemp Seed Oil</li>
        <li><span>Omega-6</span>-- 2800mg</li>
        <li><span>Omega-3</span>-- 930mg</li>
        <li><span>CBD</span>-- 250mg</li>
      </ul>
      <div class="dates">Date of Mfg.&nbsp; 18.12.2019<br>Date of Exp.&nbsp;&nbsp; 18-12-2021</div>
    </div>
  </section>

</main>
</body>
</html>
```